Income Tax Flyer - Updates Needed

Just need to update this flyer design and give it a new look. We would like to keep all the same wording but make it stand out a little more. Our selling point is the "Same Day Tax Advance up to $6,000"

Industry/Entity Type

Lending, Small Loans, Tax Services, Title Loans, Personal Loans

```html
<!DOCTYPE html>
<html lang="en">
<head>
<meta charset="UTF-8">
<title>Keystone Financial Group – Same Day Tax Advance</title>
<link href="https://fonts.googleapis.com/css2?family=Poppins:wght@400;500;600;700;800&display=swap" rel="stylesheet">
<style>
  :root{
    --green:#0f5130;
    --green-deep:#0a3a22;
    --green-mid:#1e8a50;
    --gold:#e8b53a;
    --ink:#141414;
    --grey:#3a3a3a;
    --paper:#f7f5f6;
    --card:#ffffff;
    --rule:#c9d6ce;
  }
  *{margin:0;padding:0;box-sizing:border-box}
  html,body{width:781px;height:1200px;overflow:hidden;background:var(--paper)}
  body{font-family:"Poppins",sans-serif}
  .flyer{position:relative;width:781px;height:1200px;overflow:hidden;background:var(--paper)}

  .brand{position:absolute;left:40px;top:26px;display:flex;align-items:center;gap:12px;color:var(--green)}
  .brand-dot{width:40px;height:40px;border-radius:50%;background:var(--green)}
  .brand-name{font-size:30px;font-weight:700;line-height:1}
  .brand-sub{font-size:11px;font-weight:600;letter-spacing:4px;margin-top:5px}

  .photo{position:absolute;left:40px;top:96px;width:701px;height:304px;border-radius:18px;
    background:linear-gradient(135deg,#c3ccd3 0%,#8d9db0 50%,#5f6b77 100%)}

  .headline{position:absolute;left:40px;top:350px;width:701px;height:220px;border-radius:18px;
    background:linear-gradient(120deg,var(--green) 0%,var(--green-deep) 100%);overflow:hidden;
    box-shadow:0 14px 30px rgba(10,58,34,.28)}
  .headline-rings{position:absolute;right:-70px;top:-60px;width:320px;height:320px}
  .headline-bar{position:absolute;left:0;top:0;width:10px;height:100%;background:var(--gold)}
  .headline-lead{position:absolute;left:48px;top:34px;color:#fff;font-size:36px;font-weight:700;line-height:44px;white-space:nowrap}
  .headline-amount{position:absolute;left:48px;top:84px;color:var(--gold);white-space:nowrap;line-height:1}
  .headline-amount .upto{font-size:36px;font-weight:600;color:#fff;margin-right:10px}
  .headline-amount .sum{font-size:96px;font-weight:800;letter-spacing:-1px}

  .apply{position:absolute;left:40px;top:598px;width:701px;text-align:center;color:var(--ink);font-size:28px;font-weight:700;white-space:nowrap}
  .apply .dot{display:inline-block;width:11px;height:11px;border-radius:50%;background:var(--gold);vertical-align:6px;margin:0 14px}

  .pitch{position:absolute;left:40px;top:660px;width:701px;text-align:center;color:var(--grey);font-size:25px;font-weight:500;white-space:nowrap}
  .pitch-tag{display:inline-block;margin-left:10px;background:var(--green);color:#fff;font-weight:600;padding:2px 14px;border-radius:6px;border-bottom:4px solid var(--gold)}

  .features{position:absolute;left:40px;top:734px;width:701px;display:flex;gap:25px}
  .feature{flex:1;height:180px;background:var(--card);border:1px solid var(--rule);border-radius:14px;
    display:flex;flex-direction:column;align-items:center;justify-content:center;text-align:center;
    color:var(--green);font-size:18px;font-weight:600;line-height:25px}
  .feature-icon{width:64px;height:64px;border-radius:50%;background:var(--green);display:flex;align-items:center;justify-content:center;margin-bottom:14px}
  .feature-icon svg{width:38px;height:38px}

  .contact{position:absolute;left:40px;top:944px;width:701px;height:76px;display:flex;align-items:center;justify-content:center;gap:36px}
  .contact-btn{width:262px;height:52px;border-radius:26px;background:linear-gradient(90deg,var(--green-mid),var(--green));color:#fff;font-size:20px;font-weight:600;text-align:center;line-height:52px}
  .phone{color:var(--green);font-size:24px;font-weight:700;white-space:nowrap}
  .phone svg{width:22px;height:22px;vertical-align:-3px;margin-right:12px}

  .branches{position:absolute;left:40px;top:1040px;width:701px;height:110px;display:flex;border-top:2px solid var(--green);padding-top:26px}
  .branch{flex:1;display:flex;align-items:center;padding-left:8px}
  .branch + .branch{border-left:1px solid var(--rule);padding-left:16px}
  .branch-icon{width:52px;height:52px;border-radius:50%;background:var(--green);display:flex;align-items:center;justify-content:center;margin-right:10px;flex:none}
  .branch-icon svg{width:28px;height:28px}
  .branch-text{color:var(--green);font-size:12.5px;line-height:17px;white-space:nowrap}
  .branch-text b{display:block;font-size:14px;font-weight:700;margin-bottom:2px}

  .footer-band{position:absolute;left:0;bottom:0;width:781px;height:18px;background:var(--green);border-top:4px solid var(--gold)}
</style>
</head>
<body>
<main class="flyer">
  <div class="brand">
    <span class="brand-dot"></span>
    <div>
      <div class="brand-name">Keystone</div>
      <div class="brand-sub">FINANCIAL GROUP</div>
    </div>
  </div>

  <div class="photo" role="img" aria-label="Photo of a small team of colleagues gathered around a laptop at an office table"></div>

  <section class="headline">
    <svg class="headline-rings" viewBox="0 0 320 320" fill="none" stroke="rgba(255,255,255,.10)" stroke-width="22">
      <circle cx="160" cy="160" r="140"/>
      <circle cx="160" cy="160" r="80"/>
    </svg>
    <div class="headline-bar"></div>
    <div class="headline-lead">Same Day Tax Advance</div>
    <div class="headline-amount"><span class="upto">up to</span><span class="sum">$6,000"</span></div>
  </section>

  <p class="apply"><span class="dot"></span>Apply Here For $5,000 - $6,000 Today!<span class="dot"></span></p>

  <p class="pitch">File your taxes and apply for an<span class="pitch-tag">Easy Advance!</span></p>

  <div class="features">
    <div class="feature">
      <div class="feature-icon">
        <svg viewBox="0 0 38 38" fill="none" stroke="#fff" stroke-width="2">
          <circle cx="19" cy="20" r="13"/>
          <path d="M19,12 L19,20 L25,16"/>
          <path d="M28,6 L32,9 L27,12"/>
        </svg>
      </div>
      <span>Available In<br>24 Hours or Less</span>
    </div>
    <div class="feature">
      <div class="feature-icon">
        <svg viewBox="0 0 38 38" fill="none" stroke="#fff" stroke-width="2">
          <circle cx="22" cy="13" r="8"/>
          <path d="M19,16 L25,10"/><circle cx="19.5" cy="10.5" r="1"/><circle cx="24.5" cy="15.5" r="1"/>
          <rect x="3" y="25" width="6" height="10"/>
          <path d="M9,27 L19,27 C22,27 23,30 20,30 L15,30 M9,33 L21,33 L34,28 C36,26 33,24 31,25 L24,29"/>
        </svg>
      </div>
      <span>Choose Your<br>Loan Amount</span>
    </div>
    <div class="feature">
      <div class="feature-icon">
        <svg viewBox="0 0 38 38" fill="none" stroke="#fff" stroke-width="2">
          <rect x="6" y="24" width="5" height="10"/>
          <rect x="15" y="18" width="5" height="16"/>
          <rect x="24" y="12" width="5" height="22"/>
          <path d="M5,16 L14,10 L20,12 L32,4 M27,4 L32,4 L32,9"/>
        </svg>
      </div>
      <span>Quick and Easy</span>
    </div>
  </div>

  <div class="contact">
    <div class="contact-btn">Contact Us Today!</div>
    <div class="phone">
      <svg viewBox="0 0 24 24"><path fill="var(--green)" d="M6.6 10.8a15.1 15.1 0 0 0 6.6 6.6l2.2-2.2a1 1 0 0 1 1-.25 11.4 11.4 0 0 0 3.6.57 1 1 0 0 1 1 1V20a1 1 0 0 1-1 1A17 17 0 0 1 3 4a1 1 0 0 1 1-1h3.5a1 1 0 0 1 1 1c0 1.25.2 2.45.57 3.6a1 1 0 0 1-.25 1z"/></svg>+1 800 555 0142
    </div>
  </div>

  <div class="branches">
    <div class="branch">
      <div class="branch-icon">
        <svg viewBox="0 0 34 34" fill="none" stroke="#fff" stroke-width="1.8">
          <path d="M3,10 L17,3 L31,10 Z"/><rect x="4" y="10" width="26" height="18"/>
          <path d="M9,13 V25 M14,13 V25 M20,13 V25 M25,13 V25 M2,31 H32"/>
        </svg>
      </div>
      <div class="branch-text"><b>Ohio</b>1720 Alder Lane<br>Dayton, OH 45402</div>
    </div>
    <div class="branch">
      <div class="branch-icon">
        <svg viewBox="0 0 34 34" fill="none" stroke="#fff" stroke-width="1.8">
          <path d="M17,31 C10,22 7,17 7,13 A10,10 0 0 1 27,13 C27,17 24,22 17,31 Z"/>
          <circle cx="17" cy="13" r="4"/>
        </svg>
      </div>
      <div class="branch-text"><b>Texas</b>908 Cedar Ridge Road<br>Austin, TX 78701</div>
    </div>
    <div class="branch">
      <div class="branch-icon">
        <svg viewBox="0 0 34 34" fill="none" stroke="#fff" stroke-width="1.8">
          <path d="M17,2 V6 M13,12 A4,5 0 0 1 21,12 Z"/>
          <rect x="11" y="12" width="12" height="18"/>
          <path d="M14,16 V26 M17,16 V26 M20,16 V26 M5,30 H29 M7,30 V22 H11 M27,30 V22 H23"/>
        </svg>
      </div>
      <div class="branch-text"><b>New Jersey</b>215 Harbor View Avenue<br>Trenton, NJ 08608</div>
    </div>
  </div>

  <div class="footer-band"></div>
</main>
</body>
</html>
```